Chemical Distribution Company Needs a Website

We need a website designed for an existing company based in Michigan. We have grown substantially since inception and we need our website to reflect this growth. It currently has a very mom and pop feel to it. What we do is ship chemicals in Drums, Totes, Bags, Bulk Tank Trucks, and rail from our warehouses in Toledo Oh, and Chicago il. This will be a site that strictly shows what we do and will not be E-commerced based. The final design should communicate a large business with NorthAmerican reach and worldwide sourcing capabilities.

Target Market(s)

What we sell are chemicals such as acids, solvents, oils, and salts all of which are used in the manufacturing process of various products from steel to car parts to paint to car wash soaps to food. We are trying to look like a large company that has stability and track record to go after all types of industries and manufacturers

Industry/Entity Type

It Company

Number of Pages Required

5+ page

Font styles to use
Serif
Sans Serif

Requirements
Must have
• Be Formatted for WIX as that is what we use to Host and Build. Unless you have a better idea. I would also like it to be viewed on a mobile platform which it is not now.
• Tabs for:
• Home Page (similar to "www.pellwinstock.com")
• Who we are- with subtabs for (Overview, Leadership, and Capabilities)
• Chemicals- (subtabs for (overview, Chemicals A-Z) Look at Pellwinstock.com
• Metal Working Lubricants (with a drop down identical to the products tab at "www.ravenforgeoil.com"
• Contact- Very similar to www.tarvikmenta.com/contact/
• Need to have professional photos of Chemical Facilities, Bulk Tanks Trucks, Chemical Railcars, Storage Facilities filled with Drums and Totes, a Tank Farm.
Nice to have
• Want to have our site look like a combination of tarvikmenta.com, pellwinstock.com, and brolandquintec.com

```html
<!DOCTYPE html>
<html lang="en">
<head>
<meta charset="utf-8">
<title>Norvale Chemicals</title>
<link rel="stylesheet" href="https://fonts.googleapis.com/css2?family=Raleway:wght@400;500;600&family=Arimo:wght@400&display=swap">
<style>
  :root {
    --navy-band: rgba(16, 70, 108, 0.9);
    --ring: #123f5e;
    --accent: #1e9be6;
    --logo-blue: #1c8fd8;
    --heading: #454545;
    --body-text: #3c3c3c;
    --footer: #414141;
    --social: #c9cdd1;
    --social-ring: #8f979e;
    --white: #ffffff;
  }
  * { margin: 0; padding: 0; box-sizing: border-box; }
  html, body { width: 1200px; height: 1042px; overflow: hidden; background: var(--white); }
  body { position: relative; font-family: "Arimo", Arial, sans-serif; }

  .hero {
    position: absolute; left: 0; top: 0; width: 1200px; height: 634px;
    background:
      radial-gradient(ellipse 260px 140px at 170px 590px, rgba(40,140,215,0.85), transparent 75%),
      radial-gradient(ellipse 200px 120px at 500px 580px, rgba(215,232,240,0.9), transparent 75%),
      radial-gradient(ellipse 190px 260px at 990px 470px, rgba(60,185,215,0.9), transparent 70%),
      radial-gradient(ellipse 150px 220px at 830px 500px, rgba(90,200,220,0.8), transparent 70%),
      radial-gradient(ellipse 110px 130px at 660px 400px, rgba(50,180,205,0.75), transparent 70%),
      radial-gradient(ellipse 130px 90px at 340px 220px, rgba(45,170,205,0.7), transparent 70%),
      radial-gradient(ellipse 160px 250px at 760px 280px, rgba(60,70,80,0.35), transparent 75%),
      radial-gradient(ellipse 360px 340px at 300px 380px, rgba(245,248,250,0.95), transparent 70%),
      radial-gradient(ellipse 180px 300px at 1160px 330px, rgba(30,120,170,0.8), transparent 75%),
      linear-gradient(100deg, #dfe7ec 0%, #cfdde5 35%, #9fc3d2 62%, #4ea8c6 82%, #2b7fa8 100%);
  }

  .brand {
    position: absolute; left: 0; top: 32px; width: 385px; height: 106px;
    background: rgba(255,255,255,0.93);
    display: flex; align-items: center; gap: 14px; padding-left: 48px;
  }
  .brand-mark { width: 44px; height: 44px; border-radius: 50%; background: var(--logo-blue); flex: none; }
  .brand-name {
    font-family: "Raleway", sans-serif; font-weight: 600; font-size: 25px; color: var(--logo-blue);
    letter-spacing: 0.5px; white-space: nowrap;
  }

  .topbar {
    position: absolute; left: 385px; top: 32px; width: 815px; height: 106px;
    background: var(--navy-band);
  }
  .contact-row {
    position: absolute; right: 43px; top: 15px; display: flex; align-items: center; gap: 9px;
    color: var(--white);
  }
  .call-label { font-family: "Raleway", sans-serif; font-weight: 600; font-size: 18px; }
  .call-number { font-family: "Raleway", sans-serif; font-weight: 400; font-size: 25px; margin-right: 14px; }
  .social { display: flex; gap: 14px; }
  .social span {
    width: 28px; height: 28px; border-radius: 50%; display: block;
    background: var(--social); box-shadow: inset 0 0 0 3px var(--social-ring);
  }
  .divider { position: absolute; left: 82px; right: 48px; top: 54px; height: 1px; background: rgba(255,255,255,0.35); }
  .main-nav { position: absolute; left: 82px; top: 74px; display: flex; gap: 48px; }
  .main-nav a {
    font-family: "Raleway", sans-serif; font-size: 16px; color: var(--white); text-decoration: none;
    padding-bottom: 7px; border-bottom: 3px solid transparent; white-space: nowrap;
  }
  .main-nav a.current { border-bottom-color: var(--accent); }

  .badges { position: absolute; left: 0; top: 560px; width: 1200px; height: 74px; overflow: hidden; }

  .feature { position: absolute; top: 672px; width: 300px; text-align: center; }
  .feature h2 {
    font-family: "Raleway", sans-serif; font-weight: 600; font-size: 28px; color: var(--heading);
    letter-spacing: 1px; margin-bottom: 12px;
  }
  .feature p {
    width: 252px; margin: 0 auto; font-size: 13.5px; line-height: 21px;
    color: var(--body-text); letter-spacing: 0.6px;
  }
  .more-info {
    display: inline-block; margin-top: 22px; width: 120px; height: 38px; line-height: 34px;
    border: 2px solid var(--accent); color: var(--accent); font-size: 14px; text-decoration: none; letter-spacing: 0.5px;
  }

  .site-footer {
    position: absolute; left: 0; top: 934px; width: 1200px; height: 108px; background: var(--footer);
    color: var(--white); text-align: center; font-size: 15px; letter-spacing: 0.3px;
  }
  .footer-nav { margin-top: 31px; }
  .footer-nav a { color: var(--white); text-decoration: none; }
  .footer-nav .sep { margin: 0 9px; }
  .legal { margin-top: 10px; }
</style>
</head>
<body>
  <div class="hero" role="img" aria-label="Laboratory photo: scientist in a white coat and blue gloves pipetting into a vial beside glass flasks, test tubes and a molecule model"></div>

  <div class="brand">
    <span class="brand-mark"></span>
    <span class="brand-name">NORVALE CHEMICALS</span>
  </div>

  <header class="topbar">
    <div class="contact-row">
      <svg width="24" height="24" viewBox="0 0 24 24" aria-hidden="true">
        <circle cx="12" cy="12" r="10.5" fill="none" stroke="#fff" stroke-width="1.8"/>
        <path d="M9 7.5c-.8 0-1.5.8-1.3 1.8.5 3 3 5.5 6 6 1 .2 1.8-.5 1.8-1.3l-2-1-1 1c-1.2-.6-2.3-1.7-2.9-2.9l1-1z" fill="#fff"/>
      </svg>
      <span class="call-label">CALL US</span>
      <span class="call-number">1300 555 204</span>
      <div class="social" aria-label="Social links"><span></span><span></span><span></span><span></span></div>
    </div>
    <div class="divider"></div>
    <nav class="main-nav">
      <a href="#" class="current">Home Page</a>
      <a href="#">Who we are</a>
      <a href="#">Chemicals</a>
      <a href="#">Metal Working Lubricants</a>
      <a href="#">Contact</a>
    </nav>
  </header>

  <svg class="badges" viewBox="0 0 1200 74" aria-hidden="true">
    <g fill="#fff" stroke="var(--ring)" stroke-width="4">
      <circle cx="249" cy="60" r="45"/>
      <circle cx="597" cy="60" r="45"/>
      <circle cx="946" cy="60" r="45"/>
    </g>
    <g fill="none" stroke="#1c1c1c" stroke-width="3">
      <rect x="234" y="34" width="30" height="39" rx="4"/>
      <path d="M241 45h16M241 53h16M241 61h16"/>
    </g>
    <g fill="#1c1c1c">
      <circle cx="597" cy="38" r="4.5"/>
      <rect x="591" y="44" width="12" height="30" rx="3"/>
      <circle cx="579" cy="46" r="3.5"/>
      <rect x="574" y="51" width="10" height="22" rx="3"/>
      <circle cx="615" cy="46" r="3.5"/>
      <rect x="610" y="51" width="10" height="22" rx="3"/>
    </g>
    <g fill="#1c1c1c">
      <circle cx="946" cy="56" r="15"/>
      <rect x="938" y="64" width="14" height="12"/>
    </g>
    <circle cx="944" cy="53" r="6" fill="none" stroke="#fff" stroke-width="2.5" stroke-dasharray="3 2"/>
  </svg>

  <article class="feature" style="left:99px">
    <h2>OVERVIEW</h2>
    <p>Lorem Ipsum is simply dummy text of the printing and typesetting industry. Lorem Ipsum has been the industry's standard dummy text ever since the 1500s, when an unknown</p>
    <a href="#" class="more-info">More Info</a>
  </article>
  <article class="feature" style="left:447px">
    <h2>LEADERSHIP</h2>
    <p>Lorem Ipsum is simply dummy text of the printing and typesetting industry. Lorem Ipsum has been the industry's standard dummy text ever since the 1500s, when an unknown</p>
    <a href="#" class="more-info">More Info</a>
  </article>
  <article class="feature" style="left:796px">
    <h2>CAPABILITIES</h2>
    <p>Lorem Ipsum is simply dummy text of the printing and typesetting industry. Lorem Ipsum has been the industry's standard dummy text ever since the 1500s, when an unknown</p>
    <a href="#" class="more-info">More Info</a>
  </article>

  <footer class="site-footer">
    <nav class="footer-nav">
      <a href="#">Home Page</a><span class="sep">|</span>
      <a href="#">Who we are</a><span class="sep">|</span>
      <a href="#">Chemicals</a><span class="sep">|</span>
      <a href="#">Metal Working Lubricants</a><span class="sep">|</span>
      <a href="#">Contact</a>
    </nav>
    <p class="legal">Norvale Chemicals. © 2014 All rights reserved. Site Map Privacy Policy</p>
  </footer>
</body>
</html>
```